Business Card & Email Signature Design || Upmarket + Luxury

Rima Vale Honey, a New Zealand Manuka Honey company needs a Business Card & Email Signature design.

Our logo's are attached in Gold & Black versions, feel free to be creative with how you use the logo and it's patterns in your design.

Style:
- Looking for an Elegant, Luxurious, Upmarket feel.
- Black/Matte Black Card, Gold Foil, UV Embossing

Information to Add:

- Logo
- Company Name: Rima Vale Honey
- Name: Martin Delrow
- Title: Creative Director
- Phone: +64 2815 90 617
- Email: martin@rimavalehoney.example.nz
- Website: www.rimavalehoney.example.nz

- Socials: ***For email Signature Only***
- Facebook: https://www.facebook.com/rimavalehoney/
- Instagram: https://www.instagram.com/rimavalehoney/

Target Market(s)

Asia/Europe Luxury, Upmarket

Contact Information for Business Card

- Logo
- Name: Martin Delrow
- Phone: +64 2815 90 617

Font styles to use
Other font styles liked:
• Champagne & Limousines (Attached)

Requirements
Must have
• Business Card & Email Signature Design.

Looking for a Sleek, Luxury, Upmarket Design.

```html
<!DOCTYPE html>
<html lang="en">
<head>
<meta charset="utf-8">
<title>Rima Vale Honey — Business Card</title>
<link rel="stylesheet" href="https://fonts.googleapis.com/css2?family=Lato:wght@400;700&display=swap">
<style>
  :root {
    --backdrop: #d3d4d0;
    --card-white: #ffffff;
    --card-black: #1f1f1f;
    --ink: #2f2f2f;
    --ink-soft: #7a7a7a;
    --rule: #8fa0a6;
    --gold: #c9a54e;
  }
  * { box-sizing: border-box; margin: 0; padding: 0; }
  html, body {
    width: 1200px; height: 801px; overflow: hidden;
    background: var(--backdrop);
    font-family: "Lato", sans-serif;
  }
  .stage {
    width: 1200px; height: 801px;
    display: flex; align-items: center; justify-content: center; gap: 24px;
  }
  .card {
    width: 538px; height: 308px; position: relative;
    box-shadow: 0 6px 18px rgba(0,0,0,0.12);
  }

  /* Front: white contact side */
  .card-front { background: var(--card-white); color: var(--ink); }
  .front-brand {
    position: absolute; top: 44px; right: 40px;
    display: flex; align-items: center; gap: 12px;
  }
  .brand-dot { width: 40px; height: 40px; border-radius: 50%; background: var(--ink); }
  .brand-name {
    font-size: 19px; font-weight: 400; letter-spacing: 3px;
    text-transform: uppercase; color: var(--ink);
  }
  .person { position: absolute; left: 40px; top: 100px; }
  .person-name {
    font-size: 27px; font-weight: 700; text-transform: uppercase; letter-spacing: 0.5px;
  }
  .person-title { font-size: 15px; color: var(--ink-soft); margin-top: 4px; }
  .divider {
    position: absolute; left: 40px; right: 40px; top: 176px;
    height: 1px; background: var(--rule);
  }
  .contacts {
    position: absolute; left: 40px; top: 192px; list-style: none;
    font-size: 14px; color: var(--ink-soft); line-height: 24px;
  }
  .contacts li { display: flex; align-items: center; gap: 12px; }
  .contacts svg { width: 15px; height: 15px; fill: var(--ink); flex: none; }
  .address {
    position: absolute; right: 40px; top: 192px; text-align: right;
    font-size: 15px; color: var(--ink-soft); line-height: 26px; font-style: normal;
  }

  /* Back: black gold-foil side */
  .card-back {
    background: var(--card-black);
    display: flex; flex-direction: column; align-items: center; justify-content: center; gap: 22px;
  }
  .back-dot { width: 86px; height: 86px; border-radius: 50%; border: 2px solid var(--gold); }
  .back-name {
    font-size: 30px; font-weight: 400; letter-spacing: 5px;
    text-transform: uppercase; color: var(--gold);
  }
</style>
</head>
<body>
<main class="stage">
  <section class="card card-front" aria-label="Business card front">
    <div class="front-brand">
      <span class="brand-dot"></span>
      <span class="brand-name">Rima Vale Honey</span>
    </div>
    <div class="person">
      <h1 class="person-name">Martin Delrow</h1>
      <p class="person-title">Creative Director</p>
    </div>
    <div class="divider"></div>
    <ul class="contacts">
      <li>
        <svg viewBox="0 0 24 24" aria-hidden="true"><path d="M6.6 10.8a15.1 15.1 0 0 0 6.6 6.6l2.2-2.2a1 1 0 0 1 1-.25 11.4 11.4 0 0 0 3.6.57 1 1 0 0 1 1 1V20a1 1 0 0 1-1 1A17 17 0 0 1 3 4a1 1 0 0 1 1-1h3.5a1 1 0 0 1 1 1c0 1.25.2 2.45.57 3.57a1 1 0 0 1-.25 1z"/></svg>
        +64 2815 90 617
      </li>
      <li>
        <svg viewBox="0 0 24 24" aria-hidden="true"><path d="M2 5h20v14H2z M4 7v.4l8 5.2 8-5.2V7z" fill-rule="evenodd"/></svg>
        martin@rimavalehoney.example.nz
      </li>
      <li>
        <svg viewBox="0 0 24 24" aria-hidden="true"><path d="M12 2a10 10 0 1 0 0 20 10 10 0 0 0 0-20zm-1 2.1V8H7.3A8 8 0 0 1 11 4.1zm2 0A8 8 0 0 1 16.7 8H13zM4.5 10H11v4H4.5a8 8 0 0 1 0-4zm8.5 0h6.5a8 8 0 0 1 0 4H13zm-5.7 6H11v3.9A8 8 0 0 1 7.3 16zm5.7 0h3.7a8 8 0 0 1-3.7 3.9z"/></svg>
        www.rimavalehoney.example.nz
      </li>
    </ul>
    <address class="address">
      1234 First Line Address<br>
      5678 Second Line Address
    </address>
  </section>

  <section class="card card-back" aria-label="Business card back">
    <span class="back-dot"></span>
    <p class="back-name">Rima Vale Honey</p>
  </section>
</main>
</body>
</html>
```